Medical Learning Web Design Project

The web site will be a site for medical students. It is aimed at providing a collaborative place for students to study, learn, question each other and challenge each other with learning. The site needs to have a section on the page that is for the content and this needs to be relatively clean and clinical. The surrounding elements will be informative (for the statistics, challenge etc). There will also be a slide-out screen that allows for the social/friend elements of the site.

The colour scheme needs to be clean and clinical where appropriate, but also engaging and exciting for the social/competitive elements.
Updates

Just for clarity: The site isn't expected to be 'coded' ... it is just the layered PSD files that I need.

Also, with regards to the navigation buttons ... they will never ALL be present at the same time so don't feel the need to design all on one page, but creativity around allowing few or many on a page will be an advantage ...

Thanks

Hi,

Please note that the image uploaded has been done as a wireframe by the developers. I am looking for a more creative and engaging way of presenting that content ...

Thanks

Hi all

Thank you all for the designs so far ...!

Please have a look at the new uploaded file, I am also looking not just for a 'templated home page' but also some different layouts that are represented in these wireframes. If the various layouts represented can be condensed down into 1 or 2 page templates with appropriate colour schemes to capture the type of content on the page (as already mentioned ... social .. competitive ... learning), then that will help me live the concepts better too! The friends tab for instance I have envisaged as a slider covering the screen and then sliding back when complete ... but let me see what creativity you can give to this ...!

Many thanks

Target Market(s)

Medical Students

Industry/Entity Type

Medical

Requirements
Must have
• - Not cluttered appearance
- Dynamic navigation (ie. site will be developed to only show relevant navigation buttons on each page ...)
- Navigation buttons (need to be individual buttons) will be: 'Home', 'Take the tour', 'What your peers say', 'Subscriptions', 'Free Signup', 'Contact us', 'Moderation', 'Statistics', 'Competition', 'Answer Questions', 'Post Questions', 'My profile', 'Friends'
- Please also ensure it is engaging for social elements and competitive elements (perhaps slightly different design for pages focussed on each element)
- Please also ensure that there is a masculine design and feminine design that has continuity for the site but depending on gender the design can be tailored to be more appealing (that means perhaps male social design, male competitive design, female social design, female competitive design ... without loosing continuity through the site).
- Photoshop PSD format
- Pixel perfect at least 1000 pixels wide (but the design needs to allow for various monitor sizes (only desktop or laptops ... not tablets or smart phones)

```html
<!DOCTYPE html>
<html lang="en">
<head>
<meta charset="utf-8">
<title>iNovra – The Medical Peer Review</title>
<link rel="stylesheet" href="https://fonts.googleapis.com/css2?family=Source+Sans+3:ital,wght@0,400;0,600;0,700;1,600&family=Arimo:wght@400;700&display=swap">
<style>
:root{
  --sky:#d7ebf3;
  --sky-deep:#b9dbe8;
  --navy:#2f4a68;
  --blue:#3b87b3;
  --brand:#2b6fa3;
  --slate:#4c5a6b;
  --text:#3a3f47;
  --muted:#6f7a86;
  --orange:#f59a12;
  --gold:#f7b733;
  --panel:#f2f3f4;
  --line:#cfd5da;
  --white:#ffffff;
  --slide-top:#4a79ad;
  --slide-bot:#2f5180;
}
*{box-sizing:border-box;margin:0;padding:0}
html,body{width:1200px;height:940px;overflow:hidden}
body{
  position:relative;
  font-family:"Source Sans 3",sans-serif;
  color:var(--text);
  background:
    radial-gradient(circle at 80px 270px,rgba(255,255,255,.55) 0 40px,transparent 41px),
    radial-gradient(circle at 110px 470px,rgba(255,255,255,.35) 0 60px,transparent 62px),
    radial-gradient(circle at 1140px 260px,rgba(255,255,255,.45) 0 36px,transparent 38px),
    radial-gradient(circle at 1110px 560px,rgba(255,255,255,.35) 0 50px,transparent 52px),
    radial-gradient(circle at 1150px 760px,rgba(255,255,255,.3) 0 70px,transparent 72px),
    radial-gradient(circle at 60px 760px,rgba(255,255,255,.3) 0 55px,transparent 57px),
    radial-gradient(ellipse at 50% 20%,#eef7fb 0%,var(--sky) 45%,var(--sky-deep) 100%);
}
body::before{content:"";position:absolute;left:0;top:0;width:1200px;height:4px;background:var(--navy)}
.abs{position:absolute}

/* header */
.logo{left:194px;top:38px;font-size:38px;font-weight:600;color:var(--brand);letter-spacing:.5px;line-height:1}
.logo-tag{left:191px;top:90px;font-size:12.5px;font-weight:700;color:var(--navy)}
.quote{left:330px;top:44px;width:428px;text-align:right;font-style:italic;font-weight:600;font-size:12.5px;line-height:15px;color:var(--navy)}
.quote .lead{display:block;text-align:left;padding-left:20px}
.stats-line{left:466px;top:79px;font-size:14.5px;font-style:italic;color:var(--blue)}
.web{left:792px;top:17px;font-size:10.5px;font-weight:700;color:var(--slate)}
.web-icons{left:888px;top:17px;display:flex;gap:9px}
.web-icons span{width:12px;height:12px;border-radius:2px;display:block}
.field{top:44px;width:93px;height:26px;border:1px solid #c9d2d8;background:#f3f6f8;font-size:10.5px;color:var(--slate);padding:7px 9px}
.remember{left:818px;top:79px;font-size:10px;font-weight:600;color:var(--slate);display:flex;align-items:center;gap:5px}
.remember i{width:10px;height:10px;border:1px solid #8a96a2;background:#fff;display:block}
.forgot{left:832px;top:96px;font-size:10px;font-weight:600;color:var(--slate)}
.login{left:954px;top:84px;width:59px;height:21px;border-radius:11px;background:linear-gradient(#ffd35a,var(--gold));color:var(--navy);font-size:10.5px;font-weight:700;text-align:center;line-height:21px}

/* page */
.page{left:187px;top:131px;width:826px;height:809px;background:var(--white);box-shadow:0 0 6px rgba(60,90,120,.15)}
.page-bar{left:0;top:0;width:826px;height:10px;background:var(--navy)}
.nav{left:0;top:10px;width:826px;height:51px;background:linear-gradient(#fafbfb,#eceeef);border-bottom:1px solid #dfe2e5;display:flex}
.nav-item{height:51px;border-right:1px solid #dde1e4;display:flex;flex-direction:column;align-items:center;justify-content:center;gap:3px;font-size:11.5px;color:#5b6b7b}
.nav-item svg{width:16px;height:16px;fill:var(--blue)}
.nav-item.current{color:var(--orange);font-weight:600}
.nav-item.current .tab{width:74px;height:40px;border:1px solid #bfc6cc;border-radius:6px;background:#fff;display:flex;flex-direction:column;align-items:center;justify-content:center;gap:3px;box-shadow:inset 0 -2px 3px rgba(0,0,0,.06)}
.nav-item.current svg{fill:var(--orange)}
.nav-item.last{border-right:none;font-weight:600;color:var(--slate)}
.ticker{left:0;top:61px;width:826px;height:36px;background:var(--panel)}
.ticker-text{left:15px;top:10px;font-size:11.5px;font-weight:600;color:var(--slate)}
.ticker-text u{color:var(--navy)}
.share{top:11px;height:14px;border:1px solid #aeb8c2;background:#fff;font-size:9.5px;line-height:12px;padding:0 5px;color:var(--slate)}

/* slider */
.slider{left:13px;top:114px;width:800px;height:353px;border:2px solid #dfe6ec;background:linear-gradient(var(--slide-top),var(--slide-bot));box-shadow:0 6px 8px -4px rgba(0,0,0,.25)}
.slide-title{left:48px;top:40px;color:#fff;font-size:21px;font-weight:600}
.slide-title b{font-size:26px;font-weight:600;margin-right:6px}
.features{left:55px;top:98px;list-style:none;color:#fff;font-size:15px;font-weight:600}
.features li{height:30.4px;display:flex;align-items:center;gap:10px}
.features li::before{content:"»";font-size:18px;line-height:1;margin-top:-3px}
.photo{width:166px;height:125px;border:2px solid #fff;border-radius:3px;box-shadow:0 1px 3px rgba(0,0,0,.3)}
.arrow{width:36px;height:36px;border-radius:50%;background:rgba(255,255,255,.35);display:flex;align-items:center;justify-content:center}
.arrow svg{width:14px;height:14px;stroke:#fff;stroke-width:3;fill:none}
.dots{left:320px;top:324px;width:82px;height:29px;border-radius:8px 8px 0 0;background:#3e5f8c;display:flex;align-items:center;justify-content:center;gap:8px}
.dots i{width:10px;height:10px;border-radius:50%;background:#fff;display:block}
.dots i.on{border:2px solid #fff;background:var(--orange)}

/* boxes */
.box{top:496px;width:243px;height:235px;border:1px solid #c3c9cf;border-radius:3px;background:#fff;box-shadow:0 1px 2px rgba(0,0,0,.1)}
.box-head{height:27px;border-bottom:1px solid #c3c9cf;background:linear-gradient(#fff,#f1f2f3);padding:3px 12px;font-size:18.5px;font-weight:600;color:var(--blue);line-height:21px}
.box-head.dark{color:#222;font-size:20px}
.box-head.dark small{font-size:11.5px;color:#333}
.box-head.hot{color:var(--orange)}
.box-foot{position:absolute;left:0;bottom:0;width:100%;height:17px;border-top:1px solid #c3c9cf;background:#f5f6f7;font-size:9.5px;font-weight:600;color:var(--slate);padding:2px 10px;display:flex;justify-content:space-between}
.video{left:11px;top:44px;width:219px;height:147px;background:#000;display:flex;align-items:center;justify-content:center}
.news{position:absolute;left:9px;top:40px;width:224px}
.news-item{font-family:"Arimo",sans-serif;font-size:9.5px;line-height:15px;color:#333;padding-bottom:6px;margin-bottom:8px;border-bottom:1px dotted #999}
.news-item:last-child{border-bottom:none}
.news-item b{display:block;font-size:8.5px;margin-top:1px}
.fan-head{position:absolute;left:0;top:27px;width:100%;height:43px;border-bottom:1px solid #d6dbe0}
.fan-logo{left:11px;top:6px;width:68px;height:28px;border:1px solid #b9c2ca;font-size:17px;font-weight:600;color:var(--brand);padding-left:5px;line-height:26px}
.fan-like{left:106px;top:13px;width:40px;height:18px;border:1px solid #9cb0cd;border-radius:3px;background:#eef2f8;font-size:9px;color:#3b5998;text-align:center;line-height:16px}
.fan-count{left:155px;top:8px;font-size:13.5px;font-weight:600;color:var(--brand);line-height:14px}
.fan-count small{display:block;font-size:8.5px;font-weight:400;color:var(--slate)}
.fan{position:absolute;width:47px;text-align:center;font-size:8.5px;color:var(--muted)}
.fan span{display:block;width:47px;height:46px;margin-bottom:3px;background:linear-gradient(#c9a58a,#6d5a4e)}
.footer-left{left:51px;top:913px;font-size:10px;font-weight:600;color:var(--slate)}
.footer-nav{left:592px;top:913px;width:407px;text-align:right;font-size:10px;font-weight:600;color:var(--slate);word-spacing:1px}
.footer-rule{left:187px;top:893px;width:826px;height:1px;background:#e4e8eb}
</style>
</head>
<body>

<header>
  <div class="abs logo">iNovra</div>
  <div class="abs logo-tag">The Medical Peer Review</div>
  <p class="abs quote"><span class="lead">“iNovra keeps me ahead of the game, constantly testing my knowledge...”</span>Sam, doctor in training, Northbridge University</p>
  <div class="abs stats-line">How will your stats compare</div>

  <div class="abs web">iNovra on the web:</div>
  <div class="abs web-icons">
    <span style="background:#4a6ea9"></span><span style="background:#e5473c"></span><span style="background:#55acee"></span><span style="background:#1aa3d5"></span><span style="background:#6a6a6a"></span><span style="background:#c92228"></span>
  </div>
  <div class="abs field" style="left:818px">Username</div>
  <div class="abs field" style="left:921px">Password</div>
  <div class="abs remember"><i></i>Keep me Signed in</div>
  <div class="abs forgot">Forgot your password</div>
  <div class="abs login">LOGIN</div>
</header>

<main class="abs page">
  <div class="abs page-bar"></div>
  <nav class="abs nav">
    <div class="nav-item current" style="width:95px"><div class="tab"><svg viewBox="0 0 16 16"><path d="M8 1 1 8h2v7h4v-4h2v4h4V8h2z"/></svg>Home</div></div>
    <div class="nav-item" style="width:118px"><svg viewBox="0 0 16 16"><path d="M5 1l3 3 3-3 1 1-2 2h4v11H2V4h4L4 2zM4 6v7h8V6z"/></svg>Take the tour</div>
    <div class="nav-item" style="width:156px"><svg viewBox="0 0 16 16"><circle cx="5" cy="5" r="3"/><circle cx="11" cy="4" r="2.5"/><path d="M0 15c0-4 2-6 5-6s5 2 5 6zM9 8c3 0 6 1 7 5h-5c0-2-1-4-2-5z"/></svg>What your peers say</div>
    <div class="nav-item" style="width:146px"><svg viewBox="0 0 16 16"><path d="M8 0l2.4 5.2 5.6.6-4.2 3.8 1.2 5.6L8 12.4 3 15.2l1.2-5.6L0 5.8l5.6-.6z"/></svg>Subscription Plans</div>
    <div class="nav-item" style="width:115px"><svg viewBox="0 0 16 16"><path d="M2 2h12v9H2zm1 1v7h10V3zM0 12h16v2H0z"/></svg>Free Signup</div>
    <div class="nav-item" style="width:109px"><svg viewBox="0 0 16 16"><path d="M4 0h8v16H4zm1 2v10h6V2zm3 11a1 1 0 100 2 1 1 0 000-2z"/></svg>Contact Us</div>
    <div class="nav-item last" style="width:87px"><svg viewBox="0 0 16 16"><circle cx="8" cy="8" r="8"/><path d="M7 4h2v3h3v2H9v3H7V9H4V7h3z" fill="#fff"/></svg>More</div>
  </nav>
  <div class="abs ticker">
    <div class="abs ticker-text">about 2 days ago: iNovra is now on Circlebook. Follow us <u>here.</u></div>
    <div class="abs share" style="left:568px">■ Like</div>
    <div class="abs share" style="left:612px">4K</div>
    <div class="abs share" style="left:654px;font-weight:700;color:var(--brand)">+1</div>
    <div class="abs share" style="left:687px">4K</div>
    <div class="abs share" style="left:734px;color:var(--brand);font-weight:600">Chirp</div>
    <div class="abs share" style="left:782px;color:#3a9ad0">7,231</div>
  </div>

  <section class="abs slider">
    <h1 class="abs slide-title"><b>iNovra</b>- The Medical Peer Review</h1>
    <ul class="abs features">
      <li>Test your medical knowledge</li>
      <li>Answer a vast array of medical questions</li>
      <li>Earn trophies as your knowledge increases</li>
      <li>Rate questions from peers</li>
      <li>Ask your own questions</li>
      <li>Link to your friend and check their progress</li>
      <li>29.903 Questions answered!</li>
    </ul>
    <div class="abs photo" style="left:402px;top:41px;background:linear-gradient(135deg,#fff 40%,#e9a0a0)" role="img" aria-label="Figure of a doctor beside a large red letter"></div>
    <div class="abs photo" style="left:579px;top:41px;background:linear-gradient(#fdfdfd 30%,#6c9fcf 55%,#f0b24a 85%)" role="img" aria-label="Stack of medical books with a stethoscope"></div>
    <div class="abs photo" style="left:402px;top:177px;background:linear-gradient(#f4f6f5 50%,#8fd08a 70%,#f4b36a)" role="img" aria-label="Medical icons branching from a bowl"></div>
    <div class="abs photo" style="left:579px;top:177px;background:linear-gradient(#fafafa,#e2e5e8)" role="img" aria-label="Network of medical staff figures"></div>
    <div class="abs arrow" style="left:5px;top:186px"><svg viewBox="0 0 14 14"><path d="M9 2 4 7l5 5"/></svg></div>
    <div class="abs arrow" style="left:895px;top:186px;left:auto;right:5px"><svg viewBox="0 0 14 14"><path d="M5 2l5 5-5 5"/></svg></div>
    <div class="abs dots"><i class="on"></i><i></i><i></i></div>
  </section>

  <section class="abs box" style="left:14px">
    <h2 class="box-head">How iNovra Works</h2>
    <div class="abs video"><svg width="44" height="44" viewBox="0 0 44 44"><circle cx="22" cy="22" r="20" fill="#222" stroke="#999" stroke-width="2"/><path d="M17 13l13 9-13 9z" fill="#ccc"/></svg></div>
    <div class="box-foot"><u>click to play video tour</u></div>
  </section>

  <section class="abs box" style="left:291px">
    <h2 class="box-head dark">iNovra <small>-Medical Peer Review</small></h2>
    <div class="news">
      <div class="news-item">Lorem Ipsum is simply dummy text of the printing and typesetting industry.<b>09/13/2012</b></div>
      <div class="news-item">Lorem Ipsum is simply dummy text of the printing and typesetting industry.<b>09/12/2012</b></div>
      <div class="news-item">Lorem Ipsum is simply dummy text of the printing and typesetting industry.<b>09/11/2012</b></div>
    </div>
    <div class="box-foot"><span style="color:#3ab0e2">chirper</span><span>Join the Conversation</span></div>
  </section>

  <section class="abs box" style="left:567px">
    <h2 class="box-head hot">iNovra on Circlebook:</h2>
    <div class="fan-head">
      <div class="abs fan-logo">iNovra</div>
      <div class="abs fan-like">Like</div>
      <div class="abs fan-count">6,836<small>people likes iNovra</small></div>
    </div>
    <div class="fan" style="left:13px;top:80px"><span role="img" aria-label="Profile photo of a fan"></span>Selma</div>
    <div class="fan" style="left:69px;top:80px"><span role="img" aria-label="Profile photo of a fan"></span>Marta</div>
    <div class="fan" style="left:124px;top:80px"><span role="img" aria-label="Profile photo of a fan"></span>Pavel</div>
    <div class="fan" style="left:180px;top:80px"><span role="img" aria-label="Profile photo of a fan"></span>Stella</div>
    <div class="fan" style="left:13px;top:149px"><span role="img" aria-label="Profile photo of a fan"></span>Mira</div>
    <div class="fan" style="left:69px;top:149px"><span role="img" aria-label="Profile photo of a fan"></span>Marion</div>
    <div class="fan" style="left:124px;top:149px"><span role="img" aria-label="Profile photo of a fan"></span>Dario</div>
    <div class="fan" style="left:180px;top:149px"><span role="img" aria-label="Profile photo of a fan"></span>Hana</div>
    <div class="box-foot" style="justify-content:flex-start;gap:5px;padding-left:14px"><i style="width:10px;height:10px;background:#3b5998;display:block;margin-top:1px"></i>Circlebook social plugin</div>
  </section>

  <div class="abs footer-left" style="top:782px">Copyright 2012 iNovra Limited | All Rights Reserved</div>
  <div class="abs footer-nav" style="top:782px;left:405px">Home &nbsp;|&nbsp; Take the tour &nbsp;|&nbsp; What your peers say &nbsp;|&nbsp; Subscription Plans &nbsp;|&nbsp; Free Signup &nbsp;|&nbsp; Contact Us</div>
  <div class="abs" style="left:0;top:762px;width:826px;height:1px;background:#e4e8eb"></div>
</main>

</body>
</html>
```